Korvane Nutrition Label Design

I need a label design for private label nutritional supplements.

I only need the middle section of a three part label. The ingredient information will be inserted into the left and ride side of the vector file by the manufacturer. The entire label is 15.5 cm wide by 6.3 cm tall. The space in the middle where the this label design will go is 6.3 x 6.3 cm.

I have an example of a label I have created but want replaced with a better version (-original_IMG_0949.jpeg).

I would like the label modeled on sn1792.jpg. Or modeled on berberine.jpg. I need three logos on the label: nowledge-gmp-logo-thumb-2x.jpg, non-gmo.gif, and the company logo you see at the top of the -original_IMG_0949.jpeg file (I uploaded Logo-KorvaneTin.jpg as an example of the company logo that was changed in the -original_IMG_0949.jpeg file). The logo should say Korvane Nutrition (trademark symbol), not KorvaneTin for this label.

In addition to the three logos, the label must have the company tagline "Which Tonics Suit Your Routine?" (trademark symbol). It must also say "DIETARY SUPPLEMENT"

- Use the colors from the Korvane Nutrition logo to create the label

For graphics, you can try to use the two pixelmarsh files I uploaded of the molecules. Be creative if you have an idea.

The label also must contain the following claims as you see in the -original_IMG_0949.jpg file:
Supports Dental Health* | Structural Support*
Helps Maintain Strong Bones*

The label must also feature the name of the supplement:
High Potency
Vitamin D-3
1000 IU
180 Softgels

Target Market(s)

New Supplements Users age 20-45

Industry/Entity Type

Nutrition

Requirements
Must have
• The project must have three logos on the label:
• 1) the company logo
• 2) the non-gmo logo
• 3) the GMP logo
• The label must have text for the name of the supplement:
• High Potency
• Vitamin D-3
• 1000 IU
• 180 Softgels
• The label must have the following claims:
• Supports Dental Health* | Structural Support*
• Helps Maintain Strong Bones*
• Final deliverable needs to be Photoshop Illustrator

```html
<!DOCTYPE html>
<html lang="en">
<head>
<meta charset="utf-8">
<title>Korvane Nutrition – Vitamin D-3 Label</title>
<link href="https://fonts.googleapis.com/css2?family=Nunito:wght@600;700;800;900&display=swap" rel="stylesheet">
<style>
  :root {
    --paper: #ffffff;
    --brand-blue: #1f5fa8;
    --seal-blue-dark: #1a58a3;
    --seal-blue-light: #2b6dba;
    --seal-green-dark: #17914a;
    --seal-green-light: #22a158;
    --tagline-grey: #8b8b8b;
    --badge-purple: #5b3f8f;
    --badge-green: #2f8a3a;
    --scene-sky: #a9cdea;
    --scene-sea: #3f86c4;
    --scene-land: #6f9a4a;
    --support-grey: #b9bcc0;
    --white: #ffffff;
  }
  html, body {
    margin: 0;
    padding: 0;
    width: 1200px;
    height: 2371px;
    overflow: hidden;
    background: var(--paper);
  }
  .label {
    display: block;
    width: 1200px;
    height: 2371px;
    font-family: "Nunito", sans-serif;
  }
  .brand-name { fill: var(--brand-blue); font-weight: 900; font-size: 84px; }
  .tagline { fill: var(--tagline-grey); font-weight: 800; font-size: 50px; letter-spacing: 1px; }
  .product-type { fill: var(--white); font-weight: 800; font-size: 124px; }
  .claim { fill: var(--white); font-weight: 700; font-size: 42px; letter-spacing: 0.5px; }
  .claim-rule { stroke: rgba(255,255,255,0.8); stroke-width: 2.5; }
  .potency-small { fill: var(--white); font-weight: 700; font-size: 33px; }
  .potency-name { fill: var(--white); font-weight: 800; font-size: 42px; }
  .count-number { fill: var(--white); font-weight: 900; font-size: 74px; }
  .count-unit { fill: var(--white); font-weight: 700; font-size: 28px; letter-spacing: 1px; }
</style>
</head>
<body>
<svg class="label" viewBox="0 0 1200 2371" xmlns="http://www.w3.org/2000/svg">
  <defs>
    <linearGradient id="globe-fill" x1="0" y1="0" x2="1" y2="1">
      <stop offset="0" stop-color="var(--scene-sky)"/>
      <stop offset="0.45" stop-color="var(--scene-sea)"/>
      <stop offset="1" stop-color="var(--scene-land)"/>
    </linearGradient>
    <clipPath id="seal-clip"><circle cx="603" cy="1230" r="560"/></clipPath>
    <path id="tagline-arc" d="M 120 800 A 560 560 0 0 1 1090 800"/>
  </defs>

  <!-- earth scene area -->
  <rect role="img" aria-label="Photograph of planet Earth seen from space" x="900" y="1000" width="300" height="1371" fill="url(#globe-fill)"/>

  <!-- seal supports -->
  <g class="seal-supports">
    <line x1="313" y1="1740" x2="362" y2="2000" stroke="var(--support-grey)" stroke-width="22"/>
    <line x1="892" y1="1740" x2="843" y2="2000" stroke="var(--support-grey)" stroke-width="22"/>
  </g>

  <!-- brand -->
  <g class="brand">
    <circle cx="165" cy="300" r="58" fill="var(--brand-blue)"/>
    <text class="brand-name" x="250" y="292">Korvane</text>
    <text class="brand-name" x="250" y="392">Nutrition™</text>
  </g>

  <!-- certification badges -->
  <g class="badges">
    <circle cx="1053" cy="170" r="58" fill="var(--badge-purple)"/>
    <circle cx="1053" cy="375" r="52" fill="var(--badge-green)"/>
  </g>

  <!-- tagline -->
  <text class="tagline"><textPath href="#tagline-arc" startOffset="50%" text-anchor="middle">Which Tonics Suit Your Routine?™</textPath></text>

  <!-- central seal -->
  <g class="seal" clip-path="url(#seal-clip)">
    <rect x="40" y="660" width="563" height="590" fill="var(--seal-blue-dark)"/>
    <rect x="603" y="660" width="563" height="590" fill="var(--seal-blue-light)"/>
    <rect x="40" y="1250" width="563" height="550" fill="var(--seal-green-dark)"/>
    <rect x="603" y="1250" width="563" height="550" fill="var(--seal-green-light)"/>
  </g>
  <text class="product-type" x="603" y="990" text-anchor="middle">Dietary</text>
  <text class="product-type" x="603" y="1157" text-anchor="middle">Supplement</text>

  <g class="claims">
    <text class="claim" x="603" y="1427" text-anchor="middle">Supports Dental Health*</text>
    <line class="claim-rule" x1="290" y1="1480" x2="916" y2="1480"/>
    <text class="claim" x="603" y="1540" text-anchor="middle">Helps Maintain Strong Bones*</text>
    <line class="claim-rule" x1="300" y1="1591" x2="906" y2="1591"/>
    <text class="claim" x="603" y="1650" text-anchor="middle">Structural Support*</text>
  </g>

  <!-- potency panel -->
  <g class="potency">
    <path d="M 0 1991 L 400 1991 Q 470 1991 470 2061 L 470 2371 L 0 2371 Z" fill="var(--seal-blue-dark)"/>
    <text class="potency-small" x="232" y="2055" text-anchor="middle">High Potency</text>
    <line x1="82" y1="2090" x2="382" y2="2090" stroke="var(--white)" stroke-width="2"/>
    <text class="potency-name" x="232" y="2148" text-anchor="middle">Vitamin D-3</text>
    <line x1="82" y1="2182" x2="382" y2="2182" stroke="var(--white)" stroke-width="2"/>
    <text class="potency-small" x="232" y="2232" text-anchor="middle">1000 IU</text>
  </g>

  <!-- count badge -->
  <g class="count">
    <circle cx="1070" cy="2120" r="140" fill="var(--seal-green-dark)"/>
    <text class="count-number" x="1070" y="2118" text-anchor="middle">180</text>
    <text class="count-unit" x="1070" y="2168" text-anchor="middle">SOFTGELS</text>
  </g>
</svg>
</body>
</html>
```